Investment company needing business card

We are wanting a business card which looks sharp and easy on the eye. We are thinking of having a business card with the logo embossed on it, to really make it stand out. We will only have a small amount of information of the business card, person's name, position, email address and phone number

Contact Information for Business Card

Danica Pruett
Executive Assistant
+64 21 547 3162
danicap@harwellcapital.co.nz

Requirements
Must have
• Embossed logo
Should not have
• Not to be busy

```html
<!DOCTYPE html>
<html lang="en">
<head>
<meta charset="utf-8">
<title>Harwell Capital – Business Card</title>
<link rel="stylesheet" href="https://fonts.googleapis.com/css2?family=Tinos:wght@400;700&display=swap">
<style>
  :root {
    --page-bg: #f3f3f3;
    --card-bg: #ffffff;
    --ink: #2e3436;
    --brand-grey: #5c6466;
    --band: #2d3335;
  }
  html, body {
    margin: 0;
    padding: 0;
    width: 1200px;
    height: 1200px;
    overflow: hidden;
    background: var(--page-bg);
  }
  .business-card {
    position: absolute;
    left: 250px;
    top: 401px;
    width: 699px;
    height: 398px;
    overflow: hidden;
    background: var(--card-bg);
    font-family: "Tinos", "Times New Roman", serif;
    color: var(--ink);
  }
  .brand {
    position: absolute;
    right: 47px;
    top: 46px;
    display: flex;
    align-items: center;
    gap: 10px;
  }
  .brand-mark {
    width: 46px;
    height: 46px;
    background: var(--brand-grey);
    flex: none;
  }
  .brand-name {
    font-family: "Tinos", "Times New Roman", serif;
    font-weight: 400;
    font-size: 23px;
    letter-spacing: 0.5px;
    color: var(--brand-grey);
    white-space: nowrap;
  }
  .person {
    position: absolute;
    left: 29px;
    top: 195px;
  }
  .person-name {
    margin: 0;
    font-size: 32px;
    font-weight: 700;
    line-height: 34px;
  }
  .person-role {
    margin: 0;
    font-size: 24px;
    font-weight: 400;
    line-height: 30px;
  }
  .contact {
    position: absolute;
    left: 29px;
    top: 283px;
    margin: 0;
    font-size: 24px;
    line-height: 30px;
  }
  .contact a {
    color: inherit;
    text-decoration: none;
  }
  .card-band {
    position: absolute;
    left: 0;
    bottom: 0;
    width: 100%;
    height: 30px;
    background: var(--band);
  }
</style>
</head>
<body>
  <article class="business-card">
    <div class="brand">
      <span class="brand-mark" aria-hidden="true"></span>
      <span class="brand-name">HARWELL CAPITAL</span>
    </div>
    <div class="person">
      <h1 class="person-name">Danica Pruett</h1>
      <p class="person-role">Executive Assistant</p>
    </div>
    <p class="contact">
      Call: +64 21 547 3162<br>
      <a href="mailto:danicap@harwellcapital.co.nz">danicap@harwellcapital.co.nz</a>
    </p>
    <div class="card-band"></div>
  </article>
</body>
</html>
```